Recruiting ad for Caregivers and Nurses

We need a few amazing, fun, catchy, creative recruiting ads for Caregivers and Nurses to care for homecare patients on the island of Oahu, in Hawaii. We are an in home care company called Parkdale Homecare. Our care services are provided 24/7, so we need staff that can work days, nights, weekdays, weekends. We need catchy fun ads to entice caregivers and nurses to call our office to inquire about jobs available. Our patients age range is from babies to seniors. We need caregivers and nurses for basic patient care (bathing, dressing, ambulating, preparing meals, medication reminders, light housekeeping) and complex patients (oxygen, tube feeding, injections, vents, wound care). Here are some bullets to consider including:
*Full-time and Part-time Positions Available (days, nights, weekdays, weekends)
*Sign-On Bonus Programs Offered up to $500
*Refer a Friend Bonus Program
*Holiday Pay
*2 Health Plans to Choose from
*Island-Wide Locations
*All PPE Provided (masks, gloves, etc)
*401K Program
*Tuition Benefits

```html
<!DOCTYPE html>
<html lang="en">
<head>
<meta charset="utf-8">
<title>Parkdale Homecare – We Are Hiring</title>
<link rel="stylesheet" href="https://fonts.googleapis.com/css2?family=Archivo+Black&family=Open+Sans:wght@400;700;800&family=Roboto:wght@500;700;900&display=swap">
<style>
  :root {
    --navy: #1c3a57;
    --navy-deep: #0f2a44;
    --pink: #e5336a;
    --magenta: #b51e50;
    --white: #ffffff;
    --ink: #161616;
    --sky-top: #7fa7d5;
    --sky-mid: #a9c4e3;
    --sky-low: #7c9fd0;
    --red: #e8412c;
    --lens: #0f65a3;
  }
  * { box-sizing: border-box; margin: 0; padding: 0; }
  html, body { width: 856px; height: 1200px; overflow: hidden; background: var(--sky-mid); }
  .poster {
    position: relative;
    width: 856px; height: 1200px; overflow: hidden;
    background: linear-gradient(180deg, var(--sky-top) 0%, var(--sky-mid) 55%, #9db9df 72%, var(--sky-low) 100%);
    font-family: "Roboto", Arial, sans-serif;
  }
  .abs { position: absolute; }
  .top-band { left: 0; top: 0; width: 856px; height: 62px; }
  .decor { left: 0; top: 0; width: 856px; height: 1200px; }

  .brand { left: 52px; top: 108px; width: 280px; }
  .brand-mark { width: 44px; height: 44px; background: var(--ink); border-radius: 6px; margin-bottom: 14px; margin-left: 4px; }
  .brand-name {
    font-family: "Roboto", Arial, sans-serif;
    font-weight: 900; color: var(--ink);
    font-size: 46px; line-height: 1.0; letter-spacing: -0.5px;
  }
  .brand-name span { display: block; }

  .bubble { left: 380px; top: 74px; width: 430px; height: 310px; }
  .headline { left: 383px; top: 90px; width: 420px; text-align: center; }
  .headline .we-are {
    display: block;
    font-family: "Archivo Black", "Roboto", sans-serif;
    font-size: 90px; line-height: 88px; color: var(--white); letter-spacing: -1px;
  }
  .headline .hiring {
    display: block;
    font-family: "Archivo Black", "Roboto", sans-serif;
    font-size: 92px; line-height: 84px; color: var(--pink); letter-spacing: -2px;
  }
  .headline .sub {
    margin-top: 6px;
    font-family: "Roboto", Arial, sans-serif; font-weight: 500;
    font-size: 26px; line-height: 22px; color: var(--navy); letter-spacing: -0.3px;
  }

  .halo {
    left: 258px; top: 388px; width: 336px; height: 336px; border-radius: 50%;
    background: radial-gradient(circle at 50% 45%, #b9d5f0 0%, #8fb7e4 55%, #7aa8dd 100%);
  }
  .chair-art {
    left: 328px; top: 424px; width: 214px; height: 296px; border-radius: 18px;
    background: linear-gradient(180deg, var(--pink) 0%, var(--magenta) 58%, var(--navy-deep) 100%);
  }
  .lens-art {
    left: 76px; top: 520px; width: 190px; height: 190px; border-radius: 50%;
    background: radial-gradient(circle at 40% 40%, #2f7fbf 0%, var(--lens) 55%, rgba(15,101,163,0) 72%);
    opacity: 0.85;
  }

  .schedule {
    left: 120px; top: 787px; width: 617px; height: 88px;
    background: var(--navy); border-radius: 22px;
    box-shadow: inset 0 0 0 3px var(--navy), inset 0 0 0 5px var(--white);
    color: var(--white); text-align: center;
    font-family: "Roboto", Arial, sans-serif; font-weight: 700;
    font-size: 24.5px; line-height: 30px; padding-top: 13px; letter-spacing: -0.2px;
  }

  .benefits {
    left: 48px; top: 892px; width: 760px; height: 120px;
    background: var(--magenta); border: 5px solid var(--white); border-radius: 26px;
    display: grid; grid-template-columns: 340px 1fr;
    padding: 11px 0 0 14px;
    font-family: "Open Sans", Arial, sans-serif; font-size: 16.5px; color: var(--white);
    letter-spacing: 0.3px;
  }
  .benefits ul { list-style: none; }
  .benefits li { display: flex; align-items: center; height: 21.7px; white-space: nowrap; }
  .benefits li svg { width: 16px; height: 16px; margin-right: 8px; flex: none; }

  .cta {
    left: 269px; top: 1029px; width: 319px; height: 51px; background: var(--magenta);
    color: var(--white); text-align: center;
    font-family: "Archivo Black", "Roboto", sans-serif; font-size: 30px; line-height: 51px; letter-spacing: 0.5px;
  }

  .contact {
    font-family: "Open Sans", Arial, sans-serif; font-weight: 800;
    font-size: 26px; color: var(--ink); display: flex; align-items: center; white-space: nowrap;
  }
  .contact .icon {
    width: 24px; height: 24px; border-radius: 50%; background: var(--ink);
    display: flex; align-items: center; justify-content: center; margin-right: 16px; flex: none;
  }
  .contact .icon svg { width: 15px; height: 15px; }
  .c1 { left: 60px; top: 1088px; }
  .c2 { left: 60px; top: 1124px; }
  .c3 { left: 445px; top: 1088px; }
  .c4 { left: 445px; top: 1124px; }
</style>
</head>
<body>
<main class="poster">

  <svg class="abs top-band" viewBox="0 0 856 62" aria-hidden="true">
    <polygon points="0,0 856,0 770,62 85,62" fill="var(--navy)"/>
  </svg>

  <svg class="abs decor" viewBox="0 0 856 1200" aria-hidden="true">
    <polygon points="24,323 118,310 47,374" fill="#eef1f4"/>
    <polygon points="172,352 160,410 144,397" fill="var(--red)"/>
    <circle cx="226" cy="438" r="7" fill="var(--pink)"/>
    <rect x="103" y="474" width="24" height="24" transform="rotate(45 115 486)" fill="var(--navy)"/>
    <polygon points="218,724 300,718 236,775" fill="#eef1f4"/>
    <path d="M202 545 l26 26 M228 545 l-26 26" stroke="#eef1f4" stroke-width="7" stroke-linecap="round"/>
    <circle cx="650" cy="364" r="8" fill="none" stroke="var(--pink)" stroke-width="3"/>
    <path d="M748 334 l30 30 M778 334 l-30 30" stroke="#6f93bd" stroke-width="7" stroke-linecap="round"/>
    <rect x="724" y="406" width="22" height="22" transform="rotate(45 735 417)" fill="var(--red)"/>
    <circle cx="671" cy="497" r="7" fill="none" stroke="#eef1f4" stroke-width="3"/>
    <rect x="735" y="529" width="20" height="20" transform="rotate(45 745 539)" fill="var(--navy)"/>
    <polygon points="670,636 733,651 670,659" fill="#eef1f4"/>
    <polygon points="718,671 710,722 693,710" fill="var(--red)"/>
    <path d="M628 682 l25 25 M653 682 l-25 25" stroke="#6f93bd" stroke-width="6" stroke-linecap="round"/>
    <circle cx="427" cy="557" r="185" fill="none" stroke="#c9dcf0" stroke-width="3" stroke-dasharray="180 30"/>
  </svg>

  <div class="abs brand" aria-label="Parkdale Homecare">
    <div class="brand-mark"></div>
    <p class="brand-name"><span>Parkdale</span><span>Homecare</span></p>
  </div>

  <svg class="abs bubble" viewBox="0 0 430 310" aria-hidden="true">
    <path d="M60 4 H370 A56 56 0 0 1 426 60 V196 A56 56 0 0 1 370 252 H182 C170 280 150 296 115 306 C140 290 150 270 154 252 H60 A56 56 0 0 1 4 196 V60 A56 56 0 0 1 60 4 Z"
          fill="none" stroke="var(--navy)" stroke-width="4"/>
  </svg>

  <header class="abs headline">
    <h1>
      <span class="we-are">WE ARE</span>
      <span class="hiring">HIRING!</span>
    </h1>
    <p class="sub">FULL-TIME AND PART-TIME<br>POSITIONS AVAILABLE</p>
  </header>

  <div class="abs halo" aria-hidden="true"></div>
  <div class="abs chair-art" role="img" aria-label="Illustration of an empty pink office chair on a navy swivel base, waiting to be filled"></div>
  <div class="abs lens-art" role="img" aria-label="Illustration of a blue magnifying glass searching for candidates"></div>

  <section class="abs schedule">
    FULL-TIME AND PART-TIME POSITIONS AVAILABLE<br>(DAYS, NIGHTS, WEEKDAYS, WEEKENDS)
  </section>

  <section class="abs benefits">
    <ul>
      <li><svg viewBox="0 0 16 16"><circle cx="8" cy="8" r="6.5" fill="none" stroke="#fff" stroke-width="2"/><path d="M4.5 8 l3 3 l6-7" fill="none" stroke="#fff" stroke-width="2.4" stroke-linecap="round"/></svg>Island-Wide Locations</li>
      <li><svg viewBox="0 0 16 16"><circle cx="8" cy="8" r="6.5" fill="none" stroke="#fff" stroke-width="2"/><path d="M4.5 8 l3 3 l6-7" fill="none" stroke="#fff" stroke-width="2.4" stroke-linecap="round"/></svg>All PPE Provided (masks, gloves, etc)</li>
      <li><svg viewBox="0 0 16 16"><circle cx="8" cy="8" r="6.5" fill="none" stroke="#fff" stroke-width="2"/><path d="M4.5 8 l3 3 l6-7" fill="none" stroke="#fff" stroke-width="2.4" stroke-linecap="round"/></svg>401K Program</li>
      <li><svg viewBox="0 0 16 16"><circle cx="8" cy="8" r="6.5" fill="none" stroke="#fff" stroke-width="2"/><path d="M4.5 8 l3 3 l6-7" fill="none" stroke="#fff" stroke-width="2.4" stroke-linecap="round"/></svg>Tuition Benefits</li>
    </ul>
    <ul>
      <li><svg viewBox="0 0 16 16"><circle cx="8" cy="8" r="6.5" fill="none" stroke="#fff" stroke-width="2"/><path d="M4.5 8 l3 3 l6-7" fill="none" stroke="#fff" stroke-width="2.4" stroke-linecap="round"/></svg>Sign-On Bonus Programs Offered up to $500</li>
      <li><svg viewBox="0 0 16 16"><circle cx="8" cy="8" r="6.5" fill="none" stroke="#fff" stroke-width="2"/><path d="M4.5 8 l3 3 l6-7" fill="none" stroke="#fff" stroke-width="2.4" stroke-linecap="round"/></svg>Refer a Friend Bonus Program</li>
      <li><svg viewBox="0 0 16 16"><circle cx="8" cy="8" r="6.5" fill="none" stroke="#fff" stroke-width="2"/><path d="M4.5 8 l3 3 l6-7" fill="none" stroke="#fff" stroke-width="2.4" stroke-linecap="round"/></svg>Holiday Pay</li>
      <li><svg viewBox="0 0 16 16"><circle cx="8" cy="8" r="6.5" fill="none" stroke="#fff" stroke-width="2"/><path d="M4.5 8 l3 3 l6-7" fill="none" stroke="#fff" stroke-width="2.4" stroke-linecap="round"/></svg>2 Health Plans to Choose from</li>
    </ul>
  </section>

  <div class="abs cta">JOIN OUR TEAM</div>

  <p class="abs contact c1"><span class="icon"><svg viewBox="0 0 16 16"><path d="M4 2 l3 3 l-1.5 2 c1 2 2 3 4 4 l2-1.5 l3 3 l-2 2 c-5 0-11-6-11-11 Z" fill="none" stroke="#fff" stroke-width="1.4" stroke-linejoin="round"/></svg></span>(808) 555-0142</p>
  <p class="abs contact c2"><span class="icon"><svg viewBox="0 0 16 16"><rect x="2" y="4" width="12" height="9" fill="none" stroke="#fff" stroke-width="1.4"/><path d="M2 4 l6 5 l6-5" fill="none" stroke="#fff" stroke-width="1.4"/></svg></span>jobs@parkdale.care</p>
  <p class="abs contact c3"><span class="icon"><svg viewBox="0 0 16 16"><circle cx="8" cy="8" r="6" fill="none" stroke="#fff" stroke-width="1.3"/><ellipse cx="8" cy="8" rx="2.6" ry="6" fill="none" stroke="#fff" stroke-width="1.2"/><path d="M2 8 h12 M3 5 h10 M3 11 h10" stroke="#fff" stroke-width="1"/></svg></span>www.parkdale.care</p>
  <p class="abs contact c4"><span class="icon"><svg viewBox="0 0 16 16"><path d="M8 15 C4 10 3 8 3 6 a5 5 0 0 1 10 0 c0 2-1 4-5 9 Z" fill="none" stroke="#fff" stroke-width="1.4"/><circle cx="8" cy="6" r="1.8" fill="#fff"/></svg></span>Honolulu, Oahu HI</p>

</main>
</body>
</html>
```